Double-sided business card needed - specific brief

We need a double sided business card designed for our company Radiant Trimline. Having lost a lot of weight myself, the back of the card needs to show my before and after pictures. It needs to cover the entire back side of the card. This might be with my two before pictures over set on top of my main after picture or in separate frames. I'll leave that to your artistic consideration. The front needs to have our logo with contact details centred below.

The cards will be printed by PRINTKO.com and will be rectangular, 84mm x 55mm, but with ROUNDED edges. Please therefore present your designs rectangular but with rounded edges if possible.

The card should be designed in LANDSCAPE orientation.

As well as the logo, the front of the card should have the following details:

Moira Blakewell
Weight Loss Motivator with 189lb personal loss
moira@radiant-trimline.example
+44 (0)7700 900418

The website is important so should perhaps be more bold than the rest:
www.radiant-trimline.example

My brand colours are: Pink #CD2366, Light Pink #FD88AD. Blue #1C9CB1, Light Blue #64C4DE

Target Market(s)

Women 30+

Contact Information for Business Card

As description above

Font styles to use
Sans Serif

Requirements
Must have
• Double sided.
• Back side entirely covered with my before and after pictures.
• You may wish to float my before pictures on top of my after picture or add them in different frames. I look forward to seeing your different suggestions.

```html
<!DOCTYPE html>
<html lang="en">
<head>
<meta charset="utf-8">
<title>Radiant Trimline — Business Card</title>
<link rel="stylesheet" href="https://fonts.googleapis.com/css2?family=Lato:wght@400;700;900&family=Lobster+Two:ital,wght@1,700&display=swap">
<style>
  :root {
    --backdrop: #e9dbdb;
    --card-white: #fbfbfa;
    --ink: #1d1d1d;
    --ink-soft: #5b5b5b;
    --rule: #9a9a9a;
    --brand-pink: #cd2366;
    --brand-light-pink: #fd88ad;
    --brand-blue: #1c9cb1;
    --brand-light-blue: #64c4de;
    --panel-pink: #f6c8da;
    --photo-frame: #ffffff;
  }
  * { box-sizing: border-box; margin: 0; padding: 0; }
  html, body {
    width: 1200px; height: 983px; overflow: hidden;
    background: var(--backdrop);
    font-family: "Lato", sans-serif;
  }
  .sheet {
    position: relative; width: 1200px; height: 983px;
    display: flex; align-items: center; justify-content: center; gap: 60px;
  }
  .card {
    width: 520px; height: 340px;
    border-radius: 18px;
    background: var(--card-white);
    box-shadow: 0 10px 28px rgba(90, 60, 60, 0.18);
    position: relative; overflow: hidden;
  }

  /* Front */
  .card-front {
    display: flex; flex-direction: column; align-items: center;
    padding: 78px 56px 0;
  }
  .holder-name {
    font-weight: 900; font-size: 26px; letter-spacing: 2.5px;
    color: var(--ink); text-transform: uppercase;
  }
  .holder-title {
    margin-top: 12px; font-size: 15px; letter-spacing: 1.6px;
    color: var(--ink-soft);
  }
  .contact-band {
    margin-top: 28px; width: 100%;
    border-top: 2px solid var(--rule);
    border-bottom: 2px solid var(--rule);
    display: flex; justify-content: space-between; align-items: center;
    padding: 16px 6px;
    font-size: 15px; color: var(--ink-soft); letter-spacing: 0.3px;
  }
  .website {
    margin-top: 16px; font-weight: 700; font-size: 16px;
    color: var(--brand-pink); letter-spacing: 0.4px;
  }

  /* Back */
  .card-back { padding: 20px; }
  .back-panel {
    width: 100%; height: 100%;
    background: var(--panel-pink);
    display: flex; align-items: center;
    padding: 0 20px 0 22px; gap: 18px;
  }
  .brand {
    display: flex; flex-direction: column; align-items: center; gap: 12px;
    width: 150px;
  }
  .brand-dot {
    width: 46px; height: 46px; border-radius: 50%;
    background: var(--brand-pink);
  }
  .brand-name {
    font-weight: 700; font-size: 19px; line-height: 1.15;
    color: var(--brand-pink); text-align: center; letter-spacing: 0.5px;
  }
  .journey {
    flex: 1; display: flex; gap: 8px; align-items: flex-start;
    margin-top: -20px;
  }
  .journey-step { flex: 1; display: flex; flex-direction: column; align-items: center; }
  .photo {
    width: 100%; height: 170px;
    border: 4px solid var(--photo-frame);
  }
  .photo-before { background: linear-gradient(160deg, #7f8d5a 0%, #c9c8bd 45%, #e9ecee 70%, #5c7a44 100%); }
  .photo-after  { background: linear-gradient(160deg, #d9cdb4 0%, #a97e55 40%, #2b3567 70%, #6c4a34 100%); }
  .step-label {
    margin-top: 12px;
    font-family: "Lobster Two", cursive;
    font-style: italic; font-weight: 700; font-size: 24px;
    color: var(--brand-pink);
  }
</style>
</head>
<body>
<main class="sheet">
  <section class="card card-front" aria-label="Business card front">
    <h1 class="holder-name">Moira Blakewell</h1>
    <p class="holder-title">Weight Loss Motivator with 189lb Personal Loss</p>
    <div class="contact-band">
      <span class="phone">+44 (0)7700 900418</span>
      <span class="email">moira@radiant-trimline.example</span>
    </div>
    <p class="website">www.radiant-trimline.example</p>
  </section>

  <section class="card card-back" aria-label="Business card back">
    <div class="back-panel">
      <div class="brand">
        <span class="brand-dot"></span>
        <span class="brand-name">Radiant Trimline</span>
      </div>
      <div class="journey">
        <figure class="journey-step">
          <div class="photo photo-before" role="img" aria-label="Before photo of the owner standing in a garden"></div>
          <figcaption class="step-label">Before</figcaption>
        </figure>
        <figure class="journey-step">
          <div class="photo photo-after" role="img" aria-label="After photo of the owner seated in a leather armchair"></div>
          <figcaption class="step-label">After</figcaption>
        </figure>
      </div>
    </div>
  </section>
</main>
</body>
</html>
```